Email Signature Block Design for Law Firm

I would like you to create a similar signature block for my law firm . I saw the email signature block attached as image002.png and wanted a similar design for my law firm. I want to be able to swap the portraits for each of my staff from the final design. Our law firm colors are black, gold, white, red.

Law

• i like the red circle in around the photo in the oak ridge guild design. The Tall Cedar Guild desgn is what inspired me to have a signature block design for my firm.

```html
<!DOCTYPE html>
<html lang="en">
<head>
<meta charset="utf-8">
<title>The Marlowe Firm – Email Signature</title>
<link rel="stylesheet" href="https://fonts.googleapis.com/css2?family=Cinzel:wght@400;500&family=Raleway:wght@500&family=Tinos&display=swap">
<style>
  :root {
    --black: #111111;
    --charcoal: #1e1b1b;
    --deep-red: #5a1a17;
    --red: #b3201c;
    --gold: #d6a13a;
    --gold-light: #e0ad45;
    --cream: #f5e3b8;
    --cream-deep: #efd08f;
    --white: #ffffff;
    --mist: #f3f3f3;
    --stone: #dcdcdc;
    --title-grey: #b4b4b4;
    --portrait-dark: #2e2e30;
    --portrait-light: #ebe9e6;
  }
  * { box-sizing: border-box; margin: 0; padding: 0; }
  html, body { width: 1200px; height: 400px; overflow: hidden; background: var(--white); }
  .signature {
    position: relative;
    width: 1200px;
    height: 400px;
    overflow: hidden;
  }
  .building-backdrop {
    position: absolute;
    inset: 0;
    background:
      linear-gradient(180deg, rgba(255,255,255,0) 0%, rgba(255,255,255,0) 45%, var(--cream) 80%, var(--cream-deep) 100%),
      linear-gradient(90deg, var(--white) 0%, var(--mist) 40%, var(--stone) 100%);
  }
  .brand-panel {
    position: absolute;
    inset: 0;
    clip-path: polygon(0 0, 690px 0, 506px 400px, 0 400px);
    background: linear-gradient(180deg, var(--black) 0%, var(--charcoal) 50%, var(--deep-red) 100%);
  }
  .firm-mark {
    position: absolute;
    left: 40px;
    top: 92px;
    display: flex;
    align-items: center;
    gap: 12px;
  }
  .firm-mark__square {
    width: 34px;
    height: 34px;
    background: var(--gold-light);
  }
  .firm-mark__name {
    font-family: "Cinzel", serif;
    font-weight: 500;
    font-size: 17px;
    line-height: 1.15;
    color: var(--gold-light);
    letter-spacing: 0.5px;
  }
  .person {
    position: absolute;
    left: 42px;
    top: 180px;
  }
  .person__name {
    font-family: "Cinzel", serif;
    font-weight: 400;
    font-size: 42px;
    line-height: 1;
    color: var(--gold);
    letter-spacing: 1.5px;
  }
  .person__title {
    margin-top: 8px;
    margin-left: 1px;
    font-family: "Raleway", sans-serif;
    font-weight: 500;
    font-size: 17px;
    letter-spacing: 2.5px;
    color: var(--title-grey);
  }
  .portrait-frame {
    position: absolute;
    left: 442px;
    top: 41px;
    width: 316px;
    height: 316px;
    border-radius: 50%;
    border: 7px solid var(--red);
    overflow: hidden;
  }
  .portrait-frame__photo {
    width: 100%;
    height: 100%;
    background:
      radial-gradient(ellipse 45% 55% at 50% 95%, var(--portrait-dark) 0%, var(--portrait-dark) 60%, rgba(46,46,48,0) 100%),
      linear-gradient(180deg, var(--portrait-light) 0%, #f4f2ef 100%);
  }
  .contact-list {
    position: absolute;
    right: 38px;
    top: 265px;
    list-style: none;
    font-family: "Tinos", serif;
    font-size: 20px;
    color: var(--black);
  }
  .contact-list__item {
    display: flex;
    justify-content: flex-end;
    align-items: center;
    gap: 11px;
    height: 25.5px;
  }
  .contact-list__icon {
    width: 14px;
    height: 14px;
    flex: none;
    fill: var(--black);
  }
</style>
</head>
<body>
  <main class="signature">
    <div class="building-backdrop" role="img" aria-label="Faded photo of the firm's office building with balconies and a street lamp"></div>

    <section class="brand-panel">
      <div class="firm-mark">
        <span class="firm-mark__square"></span>
        <span class="firm-mark__name">The Marlowe<br>Firm, PLLC</span>
      </div>
      <div class="person">
        <h1 class="person__name">Name Surname</h1>
        <p class="person__title">TITLE</p>
      </div>
    </section>

    <div class="portrait-frame">
      <div class="portrait-frame__photo" role="img" aria-label="Staff portrait photo"></div>
    </div>

    <ul class="contact-list">
      <li class="contact-list__item">
        <span>205-555-0148</span>
        <svg class="contact-list__icon" viewBox="0 0 24 24" aria-hidden="true"><path d="M6.6 10.8a15.1 15.1 0 0 0 6.6 6.6l2.2-2.2a1 1 0 0 1 1-.25 11.4 11.4 0 0 0 3.6.57 1 1 0 0 1 1 1V20a1 1 0 0 1-1 1A17 17 0 0 1 3 4a1 1 0 0 1 1-1h3.5a1 1 0 0 1 1 1c0 1.25.2 2.45.57 3.57a1 1 0 0 1-.25 1z"/></svg>
      </li>
      <li class="contact-list__item">
        <span>contact@marlowe-firm.com</span>
        <svg class="contact-list__icon" viewBox="0 0 24 24" aria-hidden="true"><path d="M2 5h20v2l-10 7L2 7z"/><path d="M2 9l10 7 10-7v10H2z"/></svg>
      </li>
      <li class="contact-list__item">
        <span>marlowefirmlaw</span>
        <svg class="contact-list__icon" viewBox="0 0 24 24" aria-hidden="true"><rect x="4" y="4" width="16" height="16"/></svg>
      </li>
      <li class="contact-list__item">
        <span>Harbor Point, FL</span>
        <svg class="contact-list__icon" viewBox="0 0 24 24" aria-hidden="true"><path d="M12 2a7 7 0 0 0-7 7c0 5.25 7 13 7 13s7-7.75 7-13a7 7 0 0 0-7-7zm0 9.5A2.5 2.5 0 1 1 12 6.5a2.5 2.5 0 0 1 0 5z"/></svg>
      </li>
    </ul>
  </main>
</body>
</html>
```